Business card

We need a business card design for our company based in Auckland , New Zealand called 'Kestrel + Design Ltd'. We provide architectural services. We would like to see designs that use the max. three colours (such as white, black, grey) The final design should communicate financial safety and growth."
Also I will provide our company logo. I would like to the logo to be embeded onto our business card.

Target Market(s)

new residential house, alteration & addition & light commericila design & drafting service

Industry/Entity Type

Architecture

Contact Information for Business Card

Company name: kestrel + design Ltd.
Name: Mark Telford
Job title: architectural designer & Design RQC
email address: mark@kdstudio.co.nz
mobile number: 02 5319 6620
web site: www.kdstudio.co.nz

Requirements
Must have
• My project must have..
• - embeded logo (attached company logo)
• I don't have a bigger version for our company logo, but I have one old one, so you can remove the word from it)
• - insert the attached small PDGQ logo & RQC logo
• - creative, simple and clear business card.
• - Max. three colours
Nice to have
• - Here are the samples I would like to share with you: http://www.velmorindex.com/blog/minimalistic-business-card-designs/
• I would like to have my business card like one of the creation.
Should not have
• TBA

```html
<!DOCTYPE html>
<html lang="en">
<head>
<meta charset="utf-8">
<title>Kestrel + Design Ltd — Business Card</title>
<link href="https://fonts.googleapis.com/css2?family=Montserrat:wght@400;500;600&display=swap" rel="stylesheet">
<style>
  :root {
    --ink: #0b0b0b;
    --paper: #ffffff;
    --grey: #8a8a8a;
    --badge-grey: #6f6f6f;
    --stage: #e9e9e9;
    --card-w: 620px;
    --card-h: 354px;
  }
  * { box-sizing: border-box; margin: 0; padding: 0; }
  html, body { width: 1200px; height: 900px; overflow: hidden; }
  body {
    background: var(--stage);
    font-family: "Montserrat", Arial, sans-serif;
    position: relative;
  }
  .card {
    position: absolute;
    left: 290px;
    width: var(--card-w);
    height: var(--card-h);
    border-radius: 22px;
    overflow: hidden;
    background: var(--ink);
    color: var(--paper);
  }
  .card--back { top: 70px; }
  .card--front { top: 476px; }

  .brand {
    position: absolute;
    display: flex;
    align-items: center;
    gap: 12px;
    font-weight: 500;
    font-size: 22px;
    letter-spacing: 0.2px;
    white-space: nowrap;
  }
  .brand__dot {
    width: 14px; height: 14px; border-radius: 50%;
    background: currentColor;
    flex: none;
  }
  .card--back .brand { left: 40px; top: 236px; }

  .badges {
    position: absolute;
    right: 34px;
    top: 56px;
    display: flex;
    align-items: center;
    gap: 18px;
  }
  .badge-member {
    width: 110px; height: 64px;
    background: var(--badge-grey);
  }
  .badge-licence {
    width: 92px; height: 92px; border-radius: 50%;
    background: var(--paper);
    border: 6px solid #2a2a2a;
    box-shadow: 0 0 0 3px var(--paper);
  }
  .card--back .site {
    position: absolute;
    right: 40px; top: 184px;
    font-size: 20px;
    letter-spacing: 0.5px;
  }

  .front-bg { position: absolute; inset: 0; width: 100%; height: 100%; }
  .card--front .brand { left: 36px; top: 96px; }
  .person {
    position: absolute;
    left: 96px; top: 182px;
  }
  .person__name {
    font-size: 28px; font-weight: 600; letter-spacing: 0.5px;
    text-transform: uppercase;
    white-space: nowrap;
  }
  .person__role {
    font-size: 15px; line-height: 1.3; margin-top: 2px;
  }
  .contact {
    position: absolute;
    right: 26px; top: 146px;
    list-style: none;
    color: var(--ink);
    font-size: 14px;
    line-height: 1.5;
    text-align: right;
  }
  .contact li { display: flex; justify-content: flex-end; align-items: center; gap: 8px; white-space: nowrap; }
  .contact svg { width: 12px; height: 12px; flex: none; }
</style>
</head>
<body>

<section class="card card--back" aria-label="Business card back">
  <div class="brand"><span class="brand__dot"></span>Kestrel + Design Ltd</div>
  <div class="badges">
    <div class="badge-member" role="img" aria-label="Professional membership badge"></div>
    <div class="badge-licence" role="img" aria-label="Licensed practitioner badge"></div>
  </div>
  <p class="site">www.kdstudio.co.nz</p>
</section>

<section class="card card--front" aria-label="Business card front">
  <svg class="front-bg" viewBox="0 0 620 354" preserveAspectRatio="none" aria-hidden="true">
    <path d="M450 0 C418 70 408 140 372 210 C330 292 170 318 0 310 L0 354 L620 354 L620 0 Z" fill="#8a8a8a"/>
    <path d="M478 0 C446 76 436 150 398 222 C350 306 180 336 0 330 L0 354 L620 354 L620 0 Z" fill="#ffffff"/>
    <path d="M464 0 C432 73 422 145 385 216 C340 299 175 327 0 320" fill="none" stroke="#ffffff" stroke-width="3"/>
  </svg>

  <div class="brand"><span class="brand__dot"></span>Kestrel + Design Ltd</div>

  <div class="person">
    <h1 class="person__name">Mark Telford</h1>
    <p class="person__role">Architectural designer<br>&amp; Design RQC</p>
  </div>

  <ul class="contact">
    <li>02 5319 6620
      <svg viewBox="0 0 24 24"><path fill="#0b0b0b" d="M6.6 10.8a15 15 0 0 0 6.6 6.6l2.2-2.2a1 1 0 0 1 1-.25 11.4 11.4 0 0 0 3.6.57 1 1 0 0 1 1 1V20a1 1 0 0 1-1 1A17 17 0 0 1 3 4a1 1 0 0 1 1-1h3.5a1 1 0 0 1 1 1c0 1.25.2 2.45.57 3.57a1 1 0 0 1-.25 1z"/></svg>
    </li>
    <li>mark@kdstudio.co.nz
      <svg viewBox="0 0 24 24"><rect x="2" y="5" width="20" height="14" fill="none" stroke="#0b0b0b" stroke-width="2"/><path d="M2 5l10 8 10-8" fill="none" stroke="#0b0b0b" stroke-width="2"/></svg>
    </li>
    <li>www.kdstudio.co.nz
      <svg viewBox="0 0 24 24"><circle cx="12" cy="12" r="10" fill="none" stroke="#0b0b0b" stroke-width="2"/><path d="M2 12h20M12 2c3 3 3 17 0 20M12 2c-3 3-3 17 0 20" fill="none" stroke="#0b0b0b" stroke-width="1.6"/></svg>
    </li>
  </ul>
</section>

</body>
</html>
```